Fenwick and Tarn Website

Fenwick & Tarn Website

The purpose of the Fenwick & Tarn website has 2 purposes; number 1 is to SALE the most “Rugged and Reliable products with the most versatile innovation possible. Number 2 to attract and assist territory sales manager across the United States with an easy flow website and customer sales support in the background.

Our Website Vision

This Website should be very modern and professional with a easy flow, we will use the following platform and plug-ins built with then website builder Divi Word press with Woo commerce with a sales professional CRM ( submit the plug-in of your choice for review before adding to programming) in the backend. We will provide information to the look we are looking for. All background images will be Black and White. We will provide professional images of our products that have been trimmed out and saved with a transparent background so that they can be added to a custom designed background or black and white image that will enhance the product. I want all the special tools provided in the Divi Family of tools used to give this website the WOW FACTOR. As of Now or site will be hosted on Nimbus Pier

Header design should have a Center FT Logo provided with a Hamburger Menu on the left and on the right a Search Glass Icon a Person Icon for login and register and Sales Cart Icon this could in the only Page that is Full Page Black and White image that can be blurred or ghosted back as we want the main page to be a line of 6 to 8 different Carts and Dollies to represent our products in color. Designer can take the images of our product and color correct Photoshop or whatever is needed to make it look its best. That is the landing or main image. The home page will be a slider of up to five images with 4 major messages to our customer or reasons to do business with Fenwick & Tarn. I will download 2 image to give you a idea of direction.

Slider Messages: Price Match Guarantee
Industry Best Warranty 5 Years on Frame 3 Years on Casters
Customize to fit your Surface and Application
Designed, Engineered and Manufactured Proudly in the U.S.A.

Categories/ Products Page
Carts
Dollies
Casters
Used Equipment

Categories Page

Products Page
Ratings with stars and comments
WooCommerce Composite products

Customization Page

Career Page

Contact page

Policy Page

Terms and Conditions Page

LOOK AT QUILLMARTIO.EXAMPLE WEBSITE MUST BE BETTER

Target Market(s)

We are a manufacturer of the worlds most rugged and reliable Industrial carts, dollies, hand trucks and casters. we will be selling to all types of industry's from distributors warehouse hospitals

Industry/Entity Type

Light Industrial

Coding

Coded - Design and coding required

Number of Pages Required

5+ page

Colors
ec1f27

Requirements
Must have
• Monochrome with Products colored and buttons and logo color codes in logo are Red # AF002A and Gray #5B5C5E
• Divi we own a lifetime license
• WordPress
• Woocommerce
• woocommerce composite products
• WP forms
• CRM
• Welder image is meant to be used Customization Page
Nice to have
• CRM for our 100 plus reps

```html
<!DOCTYPE html>
<html lang="en">
<head>
<meta charset="utf-8">
<title>Fenwick &amp; Tarn</title>
<link rel="stylesheet" href="https://fonts.googleapis.com/css2?family=Raleway:wght@400;600;700;800&family=Open+Sans:wght@400;600;700&display=swap">
<style>
:root{
  --red:#af002a;
  --red-bright:#c8102e;
  --gray:#5b5c5e;
  --gray-light:#dfe0e4;
  --bg-soft:#ececee;
  --ink:#1a1a1a;
  --black:#0d0d0d;
  --white:#ffffff;
  --line:#d6d6d8;
}
*{box-sizing:border-box;margin:0;padding:0}
html,body{width:1200px;height:3644px;overflow:hidden}
body{font-family:"Open Sans",Arial,sans-serif;color:var(--ink);background:var(--white);position:relative}
.block{position:absolute;left:0;width:1200px}
.btn{display:inline-flex;align-items:center;justify-content:center;border:2px solid currentColor;font-family:"Raleway",Arial,sans-serif;font-weight:700;font-size:13px;background:transparent}

/* header */
.topbar{top:0;height:64px;background:var(--black)}
.burger{position:absolute;left:99px;top:21px;width:24px}
.burger span{display:block;height:3px;background:var(--white);margin-bottom:5px}
.search{position:absolute;left:631px;top:15px;width:258px;height:30px;background:var(--white);display:flex}
.search span{flex:1;font-size:13px;font-style:italic;color:#777;padding:6px 10px}
.search i{width:36px;border-left:1px solid #999;display:flex;align-items:center;justify-content:center}
.login{position:absolute;left:920px;top:19px;color:var(--white);font-size:13px;display:flex;gap:8px;align-items:center}
.cart-icon{position:absolute;left:1066px;top:17px}
.cart-icon b{position:absolute;right:-8px;top:-2px;width:13px;height:13px;border-radius:50%;background:var(--red-bright);color:#fff;font-size:9px;text-align:center;line-height:13px}

/* hero */
.hero{top:64px;height:484px;background:radial-gradient(ellipse at 50% 60%,#f6f6f7 0%,#dcdcde 60%,#c9c9cc 100%)}
.brand{position:absolute;left:0;width:1200px;top:160px;display:flex;justify-content:center;align-items:center;gap:16px}
.brand-mark{width:54px;height:54px;background:var(--red)}
.brand-name{font-family:"Raleway",Arial,sans-serif;font-weight:800;font-size:52px;color:var(--gray);letter-spacing:1px}
.hero-text{position:absolute;top:260px;width:1200px;text-align:center;font-size:19px;color:var(--ink)}
.hero .btn{position:absolute;left:524px;top:327px;width:151px;height:44px;color:var(--red);border-width:1px;font-weight:400;font-size:13px}
.hero .btn span{color:var(--ink)}
.dots{position:absolute;top:424px;width:1200px;display:flex;justify-content:center;gap:8px}
.dots i{width:9px;height:9px;border-radius:50%;background:var(--black)}
.dots i.on{background:var(--red-bright)}

/* promo */
.promo{top:548px;height:315px}
.promo-half{position:absolute;top:0;height:315px}
.promo-half.light{left:0;width:602px;background:var(--gray-light)}
.promo-half.dark{left:602px;width:598px;background:var(--gray);color:var(--white)}
.promo-copy{position:absolute;left:82px;top:72px;z-index:2}
.promo-copy small{font-size:16px;display:block}
.promo-copy h2{font-family:"Raleway",Arial,sans-serif;font-size:44px;font-weight:700;line-height:1.1;margin-top:6px}
.light h2{color:var(--red)}
.promo-copy p{font-size:16px;margin-top:4px}
.promo-copy .btn{width:122px;height:40px;margin-top:26px}
.light .btn{color:var(--gray)}
.promo-photo{position:absolute;z-index:1}

/* product rows */
.products{background:var(--bg-soft)}
.section-title{position:absolute;top:60px;width:1200px;text-align:center;font-family:"Raleway",Arial,sans-serif;font-weight:700;font-size:35px;color:var(--red)}
.row{position:absolute;top:150px;left:99px;width:1001px;height:282px;display:flex;justify-content:space-between}
.card{position:relative;width:229px;height:282px;background:var(--white);border:1px solid var(--line);text-align:center}
.card .photo{position:absolute;left:54px;top:12px;width:120px;height:148px}
.card .stars{position:absolute;top:169px;width:100%;font-size:9px;color:var(--red-bright);letter-spacing:1px}
.card .kicker{position:absolute;top:187px;width:100%;font-size:12px}
.card h3{position:absolute;top:204px;width:100%;font-family:"Raleway",Arial,sans-serif;font-weight:700;font-size:17px}
.card hr{position:absolute;top:231px;left:54px;width:120px;border:0;border-top:1px solid #aaa}
.card .price{position:absolute;top:246px;width:100%;font-family:"Raleway",Arial,sans-serif;font-weight:700;font-size:15px;color:var(--red)}
.card .tools{position:absolute;right:0;top:30px;display:flex;flex-direction:column;gap:4px}
.card .tools i{width:39px;height:38px;display:flex;align-items:center;justify-content:center}
.arrow{position:absolute;top:285px;width:41px;height:40px;background:var(--red);display:flex;align-items:center;justify-content:center}
.arrow.prev{left:72px}.arrow.next{left:1086px}

/* feature story */
.story{top:1370px;height:436px}
.story-copy{position:absolute;left:0;top:0;width:599px;height:436px;background:var(--gray);color:var(--white)}
.story-copy h2{position:absolute;left:96px;top:60px;font-family:"Raleway",Arial,sans-serif;font-weight:700;font-size:45px}
.story-copy p{position:absolute;left:99px;top:144px;width:474px;font-size:13.5px;line-height:22px}
.story-copy .btn{position:absolute;left:99px;top:328px;width:123px;height:38px}
.story-photo{position:absolute;left:599px;top:0;width:601px;height:436px;background:linear-gradient(135deg,#e6e7ea,#c9ccd2 55%,#8f96a3)}

/* banners */
.banners{top:2314px;height:488px;background:var(--white)}
.banner{position:absolute;top:70px;width:485px;height:347px;border:1px solid #555}
.banner .b-photo{position:absolute;z-index:1}
.banner-copy{position:absolute;top:34px;z-index:2}
.banner-copy small{font-family:"Raleway",Arial,sans-serif;font-size:22px;display:block}
.banner-copy h2{font-family:"Raleway",Arial,sans-serif;font-weight:700;font-size:47px;color:var(--red);line-height:1.1}
.banner-copy p{font-size:12px;line-height:16px;margin-top:4px;width:190px}
.banner-copy .btn{margin-top:24px;width:123px;height:38px;color:var(--gray);font-size:13px}
.banner-copy .btn span{color:var(--ink)}

/* service tiles */
.services{top:3308px;height:167px;background:var(--white)}
.tile{position:absolute;top:34px;width:316px;height:87px;border:4px solid #aeb0b4;color:var(--white);display:flex;align-items:center;justify-content:space-between;padding:0 26px}
.tile.gray{background:var(--gray)}
.tile.red{background:var(--red);border-color:#d3a0ab}
.tile small{font-size:13px;display:block}
.tile strong{font-family:"Raleway",Arial,sans-serif;font-size:17px;font-weight:700;display:block;margin-top:4px}

/* footer */
.footer{top:3475px;height:169px;background:linear-gradient(90deg,#1c1c1c,#0b0b0b)}
.footer .brand{top:62px;left:99px;width:auto;justify-content:flex-start;gap:12px}
.footer .brand-mark{width:44px;height:44px;background:var(--white)}
.footer .brand-name{font-size:36px;color:var(--white)}
.foot-links{position:absolute;right:99px;top:61px;display:flex;gap:16px;color:var(--white);font-size:13px}
.copyright{position:absolute;right:99px;top:93px;color:var(--white);font-size:11px}
</style>
</head>
<body>

<header class="block topbar">
  <div class="burger"><span></span><span></span><span></span></div>
  <div class="search"><span>Search</span><i><svg width="16" height="16" viewBox="0 0 16 16"><circle cx="6.5" cy="6.5" r="5" fill="none" stroke="#111" stroke-width="2"/><path d="M10 10l5 5" stroke="#111" stroke-width="2.2"/></svg></i></div>
  <div class="login"><svg width="16" height="17" viewBox="0 0 16 17"><circle cx="8" cy="5" r="4" fill="#fff"/><path d="M0 17c0-5 3.5-7 8-7s8 2 8 7z" fill="#fff"/></svg>Login / Register</div>
  <div class="cart-icon"><svg width="24" height="22" viewBox="0 0 24 22"><path d="M1 2h4l3 12h12l3-9H7" fill="none" stroke="#fff" stroke-width="2"/><circle cx="10" cy="19" r="2" fill="#fff"/><circle cx="18" cy="19" r="2" fill="#fff"/></svg><b>1</b></div>
</header>

<section class="block hero" role="img" aria-label="Black and white warehouse interior, softly faded">
  <div class="brand"><span class="brand-mark"></span><span class="brand-name">FENWICK &amp; TARN</span></div>
  <p class="hero-text">Industry Best Warranty 5 Years on Frame 3 Years on Casters</p>
  <a class="btn"><span>Read More</span></a>
  <div class="dots"><i></i><i class="on"></i><i></i><i></i></div>
</section>

<section class="block promo">
  <div class="promo-half light">
    <div class="promo-copy">
      <small>Lorem ipsum</small>
      <h2>Heading</h2>
      <p>From $000 - $ 000</p>
      <a class="btn">Buy Now</a>
    </div>
    <div class="promo-photo" role="img" aria-label="Blue flatbed platform cart" style="left:290px;top:50px;width:276px;height:236px;background:linear-gradient(160deg,#2f5f94,#123a66)"></div>
  </div>
  <div class="promo-half dark">
    <div class="promo-copy" style="left:77px">
      <small>Lorem ipsum</small>
      <h2>Heading</h2>
      <p>From $000 - $ 000</p>
      <a class="btn">Buy Now</a>
    </div>
    <div class="promo-photo" role="img" aria-label="Red two-shelf utility cart" style="left:310px;top:30px;width:220px;height:256px;background:linear-gradient(160deg,#d42a2a,#8e1010)"></div>
  </div>
</section>

<section class="block products" style="top:863px;height:507px">
  <h2 class="section-title">Featured Products</h2>
  <div class="arrow prev"><svg width="10" height="16" viewBox="0 0 10 16"><path d="M8 1L2 8l6 7" fill="none" stroke="#fff" stroke-width="1.6"/></svg></div>
  <div class="row">
    <article class="card"><div class="photo" role="img" aria-label="Teal convertible hand truck" style="background:linear-gradient(#3aa0b8,#1f6f85)"></div><div class="stars">★★★★★</div><p class="kicker">Lorem ipsum</p><h3>Lorem Ipsum Dolor</h3><hr><p class="price">$000</p></article>
    <article class="card"><div class="photo" role="img" aria-label="Aluminum hand truck" style="background:linear-gradient(#d5d6d8,#9a9ca0)"></div><div class="tools"><i style="background:var(--red-bright)"><svg width="16" height="14" viewBox="0 0 24 22"><path d="M1 2h4l3 12h12l3-9H7" fill="none" stroke="#fff" stroke-width="2.4"/><circle cx="10" cy="19" r="2" fill="#fff"/><circle cx="18" cy="19" r="2" fill="#fff"/></svg></i><i style="background:#111"><svg width="16" height="16" viewBox="0 0 16 16"><circle cx="6.5" cy="6.5" r="5" fill="none" stroke="#fff" stroke-width="2"/><path d="M10 10l5 5" stroke="#fff" stroke-width="2.2"/></svg></i></div><div class="stars">★★★★★</div><p class="kicker">Lorem ipsum</p><h3>Lorem Ipsum Dolor</h3><hr><p class="price">$000</p></article>
    <article class="card"><div class="photo" role="img" aria-label="Black three-shelf steel cart" style="left:38px;width:152px;background:linear-gradient(#4a4543,#2a2625)"></div><div class="stars">★★★★★</div><p class="kicker">Lorem ipsum</p><h3>Lorem Ipsum Dolor</h3><hr><p class="price">$000</p></article>
    <article class="card"><div class="photo" role="img" aria-label="Red two-shelf utility cart" style="background:linear-gradient(#d42a2a,#8e1010)"></div><div class="stars">★★★★★</div><p class="kicker">Lorem ipsum</p><h3>Lorem Ipsum Dolor</h3><hr><p class="price">$000</p></article>
  </div>
  <div class="arrow next"><svg width="10" height="16" viewBox="0 0 10 16"><path d="M2 1l6 7-6 7" fill="none" stroke="#fff" stroke-width="1.6"/></svg></div>
</section>

<section class="block story">
  <div class="story-copy">
    <h2>Heading</h2>
    <p>Lorem ipsum dolor sit amet, consectetur adipiscing elit, sed do eiusmod tempor incididunt ut labore et dolore magna aliqua. Ut enim ad minim veniam, quis nostrud exercitation ullamco laboris nisi ut aliquip ex ea commodo consequat. Duis aute irure dolor in reprehenderit in volu ptate velit esse cillum dolore eu fugiat nulla pariatur. Excepteur sint occaecat cupidatat non proident, sunt in culpa qui officia deserunt mollit anim id est laborum.</p>
    <a class="btn">Buy Now</a>
  </div>
  <div class="story-photo" role="img" aria-label="Two movers wheeling a refrigerator on a hand truck in a room with boxes"></div>
</section>

<section class="block products" style="top:1806px;height:508px">
  <h2 class="section-title">Latest Products</h2>
  <div class="arrow prev"><svg width="10" height="16" viewBox="0 0 10 16"><path d="M8 1L2 8l6 7" fill="none" stroke="#fff" stroke-width="1.6"/></svg></div>
  <div class="row">
    <article class="card"><div class="photo" role="img" aria-label="Teal convertible hand truck" style="background:linear-gradient(#3aa0b8,#1f6f85)"></div><div class="stars">★★★★★</div><p class="kicker">Lorem ipsum</p><h3>Lorem Ipsum Dolor</h3><hr><p class="price">$000</p></article>
    <article class="card"><div class="photo" role="img" aria-label="Aluminum hand truck" style="background:linear-gradient(#d5d6d8,#9a9ca0)"></div><div class="stars">★★★★★</div><p class="kicker">Lorem ipsum</p><h3>Lorem Ipsum Dolor</h3><hr><p class="price">$000</p></article>
    <article class="card"><div class="photo" role="img" aria-label="Black three-shelf steel cart" style="left:38px;width:152px;background:linear-gradient(#4a4543,#2a2625)"></div><div class="stars">★★★★★</div><p class="kicker">Lorem ipsum</p><h3>Lorem Ipsum Dolor</h3><hr><p class="price">$000</p></article>
    <article class="card"><div class="photo" role="img" aria-label="Red two-shelf utility cart" style="background:linear-gradient(#d42a2a,#8e1010)"></div><div class="stars">★★★★★</div><p class="kicker">Lorem ipsum</p><h3>Lorem Ipsum Dolor</h3><hr><p class="price">$000</p></article>
  </div>
  <div class="arrow next"><svg width="10" height="16" viewBox="0 0 10 16"><path d="M2 1l6 7-6 7" fill="none" stroke="#fff" stroke-width="1.6"/></svg></div>
</section>

<section class="block banners">
  <div class="banner" style="left:99px">
    <div class="b-photo" role="img" aria-label="Blue platform cart stacked with cardboard boxes" style="left:240px;top:40px;width:228px;height:300px;background:linear-gradient(160deg,#cfa86e,#b18646 55%,#3fa6c4)"></div>
    <div class="banner-copy" style="left:23px">
      <small>Lorem Ipsum Doler Sit</small>
      <h2>Heading</h2>
      <p>Lorem ipsum dolor sit amet, consectetur adipiscing elit</p>
      <a class="btn"><span>Buy Now</span></a>
    </div>
  </div>
  <div class="banner" style="left:616px">
    <div class="b-photo" role="img" aria-label="Hand truck loaded with cardboard boxes" style="left:14px;top:14px;width:188px;height:322px;background:linear-gradient(160deg,#9aa3ad,#c79c5f 45%,#a8793d)"></div>
    <div class="banner-copy" style="left:217px">
      <small>Lorem Ipsum Doler Sit</small>
      <h2>Heading</h2>
      <p>Lorem ipsum dolor sit amet, consectetur adipiscing elit</p>
      <a class="btn"><span>Buy Now</span></a>
    </div>
  </div>
</section>

<section class="block products" style="top:2802px;height:506px">
  <h2 class="section-title">Upcoming Products</h2>
  <div class="arrow prev"><svg width="10" height="16" viewBox="0 0 10 16"><path d="M8 1L2 8l6 7" fill="none" stroke="#fff" stroke-width="1.6"/></svg></div>
  <div class="row">
    <article class="card"><div class="photo" role="img" aria-label="Teal convertible hand truck" style="background:linear-gradient(#3aa0b8,#1f6f85)"></div><div class="stars">★★★★★</div><p class="kicker">Lorem ipsum</p><h3>Lorem Ipsum Dolor</h3><hr><p class="price">$000</p></article>
    <article class="card"><div class="photo" role="img" aria-label="Aluminum hand truck" style="background:linear-gradient(#d5d6d8,#9a9ca0)"></div><div class="stars">★★★★★</div><p class="kicker">Lorem ipsum</p><h3>Lorem Ipsum Dolor</h3><hr><p class="price">$000</p></article>
    <article class="card"><div class="photo" role="img" aria-label="Black three-shelf steel cart" style="left:38px;width:152px;background:linear-gradient(#4a4543,#2a2625)"></div><div class="stars">★★★★★</div><p class="kicker">Lorem ipsum</p><h3>Lorem Ipsum Dolor</h3><hr><p class="price">$000</p></article>
    <article class="card"><div class="photo" role="img" aria-label="Red two-shelf utility cart" style="background:linear-gradient(#d42a2a,#8e1010)"></div><div class="stars">★★★★★</div><p class="kicker">Lorem ipsum</p><h3>Lorem Ipsum Dolor</h3><hr><p class="price">$000</p></article>
  </div>
  <div class="arrow next"><svg width="10" height="16" viewBox="0 0 10 16"><path d="M2 1l6 7-6 7" fill="none" stroke="#fff" stroke-width="1.6"/></svg></div>
</section>

<section class="block services">
  <div class="tile gray" style="left:99px">
    <div><small>Lorem ipsum</small><strong>Lorem Ipsum Dolor</strong></div>
    <svg width="54" height="54" viewBox="0 0 54 54"><path d="M12 6l8 8-5 6c3 8 9 14 17 17l6-5 8 8-6 7C22 47 7 32 5 12z" fill="#fff"/><path d="M30 8a16 16 0 0 1 16 16M30 15a9 9 0 0 1 9 9" fill="none" stroke="#fff" stroke-width="3"/></svg>
  </div>
  <div class="tile red" style="left:442px">
    <div><small>Lorem ipsum</small><strong>Lorem Ipsum Dolor</strong></div>
    <svg width="56" height="52" viewBox="0 0 56 52"><path d="M2 4h9l7 30h30l6-22H14" fill="none" stroke="#fff" stroke-width="4"/><path d="M22 18h28M24 26h24" stroke="#fff" stroke-width="3"/><circle cx="23" cy="44" r="4" fill="#fff"/><circle cx="43" cy="44" r="4" fill="#fff"/></svg>
  </div>
  <div class="tile gray" style="left:784px">
    <div><small>Lorem ipsum</small><strong>Lorem Ipsum Dolor</strong></div>
    <svg width="56" height="50" viewBox="0 0 56 50"><path d="M10 14L38 3l4 11" fill="none" stroke="#fff" stroke-width="3"/><rect x="4" y="14" width="48" height="32" rx="3" fill="#fff"/><rect x="34" y="24" width="20" height="12" rx="2" fill="#5b5c5e"/><circle cx="41" cy="30" r="2.5" fill="#fff"/></svg>
  </div>
</section>

<footer class="block footer">
  <div class="brand"><span class="brand-mark"></span><span class="brand-name">FENWICK &amp; TARN</span></div>
  <nav class="foot-links"><span>Customization</span><span>Career</span><span>Contact</span><span>Policy</span><span>Terms and Conditions</span></nav>
  <p class="copyright">©2019 By Fenwick &amp; Tarn. All rights reserved</p>
</footer>

</body>
</html>
```